Business Card Design

We Import cars and commercial vehicles, we have been in business around 12 years, we are based in Christchurch, New Zealand.
I really like the web address on card, possibly right along the bottom of the card?
We specialize in commercial vans, maybe worth a mention?
The logo has the name in it so probably don't need to have twice?

I really like a clean smart look, not too cluttered

Industry/Entity Type

Business

Contact Information for Business Card

RQL MOTORS, Derek Holloway, Managing Director
web address: www.rqlmotorsnz.com
cell phone. 021 485 912

Requirements
Must have
• the logo, and all the contact details.

Forgot to add my email address, derek@rqlmotorsnz.com
Nice to have
• Just thinking as the card is looking a little empty maybe somewhere written what we do? 'Specializing in commercial vans'
Not sure but we import Japanese vehicles, possibly adding some brands like Velkara Poremo Ketsu Brivon etc? Not sure on that one.

```html
<!DOCTYPE html>
<html lang="en">
<head>
<meta charset="utf-8">
<title>RQL Motors – Business Card</title>
<link href="https://fonts.googleapis.com/css2?family=Quicksand:wght@400;500;700&display=swap" rel="stylesheet">
<style>
  :root {
    --bg: #e3e3e3;
    --card: #f2f2f2;
    --ink: #1c1c1c;
    --ink-soft: #4a4a4a;
    --muted: #6b6b6b;
    --rule: #8a8a8a;
    --band-dark: #2b2b2b;
    --band-mid: #6d6d6d;
  }
  * { box-sizing: border-box; margin: 0; padding: 0; }
  html, body {
    width: 1200px;
    height: 900px;
    overflow: hidden;
    background: var(--bg);
    font-family: "Quicksand", sans-serif;
    color: var(--ink);
  }
  .card {
    position: absolute;
    left: 150px;
    top: 175px;
    width: 900px;
    height: 550px;
    background: var(--card);
    box-shadow: 0 10px 30px rgba(0,0,0,0.12);
    overflow: hidden;
  }
  .brand {
    position: absolute;
    left: 70px;
    top: 186px;
    display: flex;
    align-items: center;
    gap: 14px;
  }
  .brand-mark {
    width: 18px;
    height: 18px;
    border-radius: 50%;
    background: var(--ink);
  }
  .brand-name {
    font-weight: 700;
    font-size: 34px;
    line-height: 1;
    white-space: nowrap;
    color: var(--ink);
  }
  .tagline {
    position: absolute;
    left: 70px;
    top: 420px;
    font-size: 22px;
    font-weight: 400;
    color: var(--ink-soft);
  }
  .divider {
    position: absolute;
    left: 440px;
    top: 140px;
    width: 2px;
    height: 250px;
    background: var(--rule);
  }
  .identity {
    position: absolute;
    left: 490px;
    top: 150px;
  }
  .person-name {
    font-size: 46px;
    font-weight: 400;
    line-height: 1.1;
    white-space: nowrap;
  }
  .person-name strong { font-weight: 700; }
  .person-role {
    font-size: 22px;
    color: var(--muted);
    margin-top: 4px;
  }
  .contacts {
    position: absolute;
    left: 470px;
    top: 270px;
    list-style: none;
  }
  .contact {
    display: flex;
    align-items: center;
    gap: 22px;
    height: 46px;
    font-size: 22px;
    font-weight: 500;
    color: var(--ink-soft);
    white-space: nowrap;
  }
  .contact svg { width: 22px; height: 22px; flex: none; }
  .base-band {
    position: absolute;
    left: 0; right: 0; bottom: 0;
    height: 46px;
    background: var(--band-dark);
    border-top: 10px solid var(--band-mid);
  }
</style>
</head>
<body>
  <div class="card">
    <div class="brand">
      <span class="brand-mark"></span>
      <span class="brand-name">RQL MOTORS</span>
    </div>
    <p class="tagline">Specializing in commercial vans</p>

    <div class="divider"></div>

    <div class="identity">
      <h1 class="person-name">Derek <strong>Holloway</strong></h1>
      <p class="person-role">Managing Director</p>
    </div>

    <ul class="contacts">
      <li class="contact">
        <svg viewBox="0 0 24 24" fill="none" stroke="#333" stroke-width="2"><rect x="6" y="2" width="12" height="20" rx="2"/><line x1="11" y1="18" x2="13" y2="18"/></svg>
        021 485 912
      </li>
      <li class="contact">
        <svg viewBox="0 0 24 24" fill="#333"><path d="M2 5h20v14H2z"/><path d="M2 5l10 8 10-8" fill="none" stroke="#f2f2f2" stroke-width="1.8"/></svg>
        derek@rqlmotorsnz.com
      </li>
      <li class="contact">
        <svg viewBox="0 0 24 24" fill="#333"><path d="M12 2a7 7 0 0 0-7 7c0 5 7 13 7 13s7-8 7-13a7 7 0 0 0-7-7zm0 9.5A2.5 2.5 0 1 1 12 6.5a2.5 2.5 0 0 1 0 5z"/></svg>
        www.rqlmotorsnz.com
      </li>
    </ul>

    <div class="base-band"></div>
  </div>
</body>
</html>
```